Visitenkarten-Design für Hotel und Restaurant in der Fußgängerzone
Zielgruppe
Hotel und Restaurant in der Fußgängerzone, zwei Gehminuten zum Bodensee.
Neu renoviertes Hotel/Restaurant (z.B.Boxspringbett, Holzboden, USB Steckdosen).
Übernachtung mit Frühstück im Einzel,-Doppel,- oder Komfortzimmer (für 3 Personen).
Restaurant mit regionaler Küche. Besondere saisonale Zutaten unserer Nachbarländer als Specials.
Touristen im Sommer Durchschnittalter: 50 Jahre, sportlich, modern, gut betucht.
Einwohner der Stadt im Winter, Alter zwischen 25 und 65 Jahre, viele davon Hausbesitzer, Segelboot Besitzer etc.
Aufgabenstellung
Farbkonzept im Restaurant:
warm- weiße Wände, dunkle Holzmöbel, rote Barelemente, weiß-kupferfarbene Lampen.
Würden uns etwas minimalistisches wünschen, trotzdem mit einem Wow Effekt.
Sei es ein ausgeschnittenes Logo, abgerundete Ecken, besonderes Material usw.
Dateianhänge sind nur für´s bessere Verständnis, muss nicht zwingend als Vorgabe gesehen werden.
Vorderseite:
Logo
Hotel & Restaurant (kann, muss aber nicht draufstehen.)
zum Anker
Überlingen

```html
<!DOCTYPE html>
<html lang="de">
<head>
<meta charset="utf-8">
<title>zum Anker – Visitenkarte</title>
<link rel="stylesheet" href="https://fonts.googleapis.com/css2?family=Open+Sans:wght@400;700&family=Quicksand:wght@400&display=swap">
<style>
  :root {
    --ink: #000000;
    --paper: #ffffff;
    --mist: #e4e5e7;
    --rule: #111111;
  }
  * { margin: 0; padding: 0; box-sizing: border-box; }
  html, body { width: 979px; height: 1200px; overflow: hidden; background: var(--paper); }
  .canvas { position: relative; width: 979px; height: 1200px; background: var(--paper); font-family: "Open Sans", sans-serif; }

  .card { position: absolute; left: 76px; width: 819px; overflow: hidden; }
  .card--front { top: 89px; height: 500px; background: var(--ink); color: var(--paper); }
  .card--back { top: 612px; height: 499px; background: var(--paper); border: 1.5px solid var(--rule); color: var(--ink); }

  .brand { position: absolute; text-align: center; }
  .brand__mark { display: block; margin: 0 auto; border-radius: 50%; }
  .brand__name { display: block; font-family: "Open Sans", sans-serif; font-weight: 700; line-height: 1; white-space: nowrap; letter-spacing: -0.5px; }
  .brand__place { display: flex; align-items: center; justify-content: center; font-family: "Quicksand", sans-serif; font-weight: 400; }
  .brand__place::before, .brand__place::after { content: ""; display: block; height: 1.5px; background: currentColor; }

  .card--front .brand { left: 0; right: 0; top: 98px; }
  .card--front .brand__mark { width: 150px; height: 150px; border: 16px solid var(--paper); }
  .card--front .brand__name { margin-top: 56px; font-size: 66px; }
  .card--front .brand__place { margin-top: 20px; font-size: 23px; letter-spacing: 3px; }
  .card--front .brand__place::before, .card--front .brand__place::after { width: 67px; margin: 0 22px; }

  .card--back .brand { left: 30px; width: 320px; top: 104px; }
  .card--back .brand__mark { width: 124px; height: 124px; border: 13px solid var(--ink); }
  .card--back .brand__name { margin-top: 46px; font-size: 52px; }
  .card--back .brand__place { margin-top: 14px; font-size: 19px; letter-spacing: 2.5px; }
  .card--back .brand__place::before, .card--back .brand__place::after { width: 55px; margin: 0 16px; }

  .divider { position: absolute; left: 360px; top: 66px; width: 1.5px; height: 355px; background: var(--rule); }

  .backdrop-circle { position: absolute; left: 594px; top: 305px; width: 262px; height: 262px; border-radius: 50%; background: var(--mist); }

  .contact { position: absolute; left: 408px; top: 150px; list-style: none; font-size: 21px; line-height: 25px; }
  .contact__item { display: flex; align-items: flex-start; position: relative; }
  .contact__item + .contact__item { margin-top: 18px; }
  .contact__icon { width: 26px; height: 26px; flex: none; margin-right: 16px; }
  .contact__item--address .contact__icon { margin-top: 4px; }
</style>
</head>
<body>
<div class="canvas">

  <section class="card card--front" aria-label="Vorderseite">
    <div class="brand">
      <span class="brand__mark"></span>
      <span class="brand__name">zum Anker</span>
      <span class="brand__place">Überlingen</span>
    </div>
  </section>

  <section class="card card--back" aria-label="Rückseite">
    <div class="backdrop-circle"></div>

    <div class="brand">
      <span class="brand__mark"></span>
      <span class="brand__name">zum Anker</span>
      <span class="brand__place">Überlingen</span>
    </div>

    <div class="divider"></div>

    <ul class="contact">
      <li class="contact__item">
        <svg class="contact__icon" viewBox="0 0 24 24" aria-hidden="true"><path fill="#000" d="M6.6 10.8c1.4 2.8 3.8 5.1 6.6 6.6l2.2-2.2c.3-.3.7-.4 1-.2 1.1.4 2.3.6 3.6.6.6 0 1 .4 1 1V20c0 .6-.4 1-1 1C10.6 21 3 13.4 3 4c0-.6.4-1 1-1h3.5c.6 0 1 .4 1 1 0 1.3.2 2.5.6 3.6.1.3 0 .7-.2 1l-2.3 2.2z"/></svg>
        <span>07 551 302 418</span>
      </li>
      <li class="contact__item">
        <svg class="contact__icon" viewBox="0 0 24 24" aria-hidden="true"><rect x="2" y="5" width="20" height="14" fill="#000"/><path d="M2.5 5.5 12 13l9.5-7.5M2.5 18.5 9.5 11.5M21.5 18.5l-7-7" stroke="#fff" stroke-width="1.4" fill="none"/></svg>
        <span>info@zum-anker-ueberlingen.de</span>
      </li>
      <li class="contact__item contact__item--address">
        <svg class="contact__icon" viewBox="0 0 24 24" aria-hidden="true"><path fill="#000" d="M12 1.5c-4.4 0-8 3.4-8 7.8 0 5.4 8 13.2 8 13.2s8-7.8 8-13.2c0-4.4-3.6-7.8-8-7.8zm0 11a3.3 3.3 0 1 1 0-6.6 3.3 3.3 0 0 1 0 6.6z"/></svg>
        <span>Hafengasse 12<br>88662 Überlingen</span>
      </li>
      <li class="contact__item">
        <svg class="contact__icon" viewBox="0 0 24 24" aria-hidden="true"><g fill="none" stroke="#000" stroke-width="1.8"><circle cx="12" cy="12" r="10"/><ellipse cx="12" cy="12" rx="4.2" ry="10"/><path d="M2 12h20M3.5 7h17M3.5 17h17M12 2v20"/></g></svg>
        <span>www.zum-anker-ueberlingen.de</span>
      </li>
    </ul>
  </section>

</div>
</body>
</html>
```